Wills & Estates legal firm needing A4 presentation folder design

We need a more corporate but family orientated looking presentation folder incorporating existing logo. Needs to be clean lines but warm not clinical. Will contain all documents a family needs when someone dies. Not looking for traditional legal symbols of scales etc. Potential that the design can flow through to letterhead, document front covers, brochures, business cards etc for a complete corporate identity. We are only a firm of one fee earner and cater to a mum and dad market

Industry/Entity Type

Law Firm

Font styles to use
Other font styles liked:
• Univers LT std 57 cn

Colors
ec1f27
848484

Requirements
Must have
• Existing logo
• Area for contact details on back of folder
• Incorporating existing red an grey colours
Should not have
• legal symbols

```html
<!DOCTYPE html>
<html lang="en">
<head>
<meta charset="utf-8">
<title>Heritage Counsel – Presentation Folder</title>
<link href="https://fonts.googleapis.com/css2?family=Open+Sans:wght@400;600;700&family=Roboto+Condensed:wght@400&display=swap" rel="stylesheet">
<style>
  :root{
    --brand-red:#ec1f27;
    --brand-grey:#848484;
    --stage:#232323;
    --white:#ffffff;
    --ink-soft:#6d6d6d;
  }
  *{margin:0;padding:0;box-sizing:border-box}
  html,body{width:1200px;height:1200px;overflow:hidden;background:var(--stage)}
  body{position:relative;font-family:"Open Sans",Arial,sans-serif;color:var(--white)}

  .spread{position:absolute;width:719px;height:540px;display:flex}
  .spread--front{left:74px;top:34px}
  .spread--inner{left:348px;top:625px}
  .panel{position:relative;width:50%;height:100%;overflow:hidden}

  .stage-label{position:absolute;font-size:31px;font-weight:400;color:var(--white)}
  .stage-label--front{left:846px;top:276px}
  .stage-label--inner{left:214px;top:872px}

  .wordmark{font-family:"Open Sans",Arial,sans-serif;font-weight:400;white-space:nowrap;letter-spacing:-0.2px}

  /* back cover */
  .back-cover{background:var(--brand-red)}
  .map-area{position:absolute;left:64px;top:112px;width:232px;height:94px;border-radius:40px;background:rgba(255,255,255,0.85)}
  .back-logo{position:absolute;left:17px;bottom:21px;font-size:12px;color:var(--white)}
  .contact-block{position:absolute;bottom:16px;border-left:1px solid var(--white);padding-left:4px;font-family:"Roboto Condensed",Arial,sans-serif;font-size:6px;line-height:8px;color:var(--white);white-space:nowrap}
  .contact-block--address{left:128px}
  .contact-block--phone{left:218px}
  .contact-block--web{left:273px}

  /* front cover */
  .front-cover{background:var(--white)}
  .front-art{position:absolute;left:0;top:0;width:359px;height:540px}
  .front-brand{position:absolute;top:56px;left:0;width:100%;text-align:center;padding-left:8px}
  .front-brand .wordmark{font-size:24px;color:var(--brand-red);line-height:32px}
  .tagline{font-size:8.4px;color:var(--ink-soft);margin-top:0}

  /* inner left */
  .welcome-panel{background:var(--brand-grey)}
  .skyline-photo{position:absolute;left:0;top:0;width:100%;height:300px;background:linear-gradient(180deg,#5f5f5f 0%,#8a8a8a 45%,#a6a6a6 70%,var(--brand-grey) 100%)}
  .inner-brand{position:absolute;right:14px;top:14px;font-size:13px;color:var(--white)}
  .welcome{position:absolute;left:40px;top:288px;width:280px}
  .welcome-kicker{font-size:9.5px;line-height:10px}
  .welcome-title{display:flex;align-items:center;gap:3px;padding-left:12px}
  .welcome-title h1{font-size:12px;font-weight:700;line-height:14px;letter-spacing:-0.3px}
  .welcome-title span{flex:1;height:1px;background:#c9c9c9}
  .welcome-body{margin-top:10px;font-size:5.1px;line-height:8.8px}
  .welcome-body p{margin-bottom:8.8px}
  .welcome-body ul{list-style:none;margin-bottom:8.8px}
  .site-pill{position:absolute;left:124px;top:517px;width:112px;height:9px;border-radius:5px;background:var(--white);color:#333;font-size:5.4px;letter-spacing:1.2px;text-align:center;line-height:9px;font-weight:600}

  /* inner right */
  .pocket-panel{background:var(--white)}
  .pocket{position:absolute;left:21px;top:404px;width:339px;height:136px;background:var(--brand-red);border-top-left-radius:38px;box-shadow:0 -2px 6px rgba(0,0,0,0.18)}
</style>
</head>
<body>

<section class="spread spread--front">
  <div class="panel back-cover">
    <div class="map-area" role="img" aria-label="White world map silhouette"></div>
    <span class="back-logo wordmark">Heritage Counsel</span>
    <div class="contact-block contact-block--address">Elm Park Center 10290<br>Road Westfield, Ohio 45100</div>
    <div class="contact-block contact-block--phone">(005) 410-2290<br>(513) 555-0148</div>
    <div class="contact-block contact-block--web">hello@heritagecounsel.com<br>www.heritagecounsel.com</div>
  </div>

  <div class="panel front-cover">
    <svg class="front-art" viewBox="0 0 449 675" preserveAspectRatio="none">
      <defs>
        <linearGradient id="swoosh-fade" gradientUnits="userSpaceOnUse" x1="300" y1="230" x2="380" y2="620">
          <stop offset="0" stop-color="#ffffff"/>
          <stop offset="0.3" stop-color="#fbe4de"/>
          <stop offset="1" stop-color="#ef6a52"/>
        </linearGradient>
        <linearGradient id="floor-grey" x1="0" y1="0" x2="0" y2="1">
          <stop offset="0" stop-color="#bdbdbd"/>
          <stop offset="1" stop-color="#7e7e7e"/>
        </linearGradient>
        <linearGradient id="tower-blue" x1="0" y1="0" x2="1" y2="1">
          <stop offset="0" stop-color="#5f9fd0"/>
          <stop offset="0.5" stop-color="#2f6a9e"/>
          <stop offset="1" stop-color="#1d4266"/>
        </linearGradient>
        <linearGradient id="meeting-tone" x1="0" y1="0" x2="1" y2="1">
          <stop offset="0" stop-color="#e9edf1"/>
          <stop offset="1" stop-color="#9aa4ad"/>
        </linearGradient>
      </defs>
      <circle cx="100" cy="400" r="336" fill="url(#swoosh-fade)"/>
      <path d="M110 660 Q250 702 392 612 L449 560 L449 675 L110 675 Z" fill="#ffffff"/>
      <rect x="0" y="545" width="160" height="130" fill="url(#floor-grey)"/>
      <circle cx="110" cy="440" r="207" fill="none" stroke="var(--brand-red)" stroke-width="4"/>
      <circle cx="110" cy="440" r="200" fill="url(#tower-blue)" role="img" aria-label="Glass office tower photograph"/>
      <path d="M110 648 Q250 690 392 612" fill="none" stroke="var(--brand-red)" stroke-width="4"/>
      <circle cx="265" cy="297" r="66" fill="#ffffff" stroke="var(--brand-red)" stroke-width="4"/>
      <circle cx="265" cy="297" r="60" fill="url(#meeting-tone)" role="img" aria-label="Photograph of two advisers meeting at a desk"/>
    </svg>
    <div class="front-brand">
      <div class="wordmark">Heritage Counsel</div>
      <div class="tagline">The trusted online marketplace</div>
    </div>
  </div>
</section>
<div class="stage-label stage-label--front">Front</div>

<section class="spread spread--inner">
  <div class="panel welcome-panel">
    <div class="skyline-photo" role="img" aria-label="Greyscale photograph looking up between glass towers"></div>
    <div class="inner-brand wordmark">Heritage Counsel</div>
    <article class="welcome">
      <div class="welcome-kicker">Welcome to</div>
      <div class="welcome-title"><h1>Heritage Counsel</h1><span></span></div>
      <div class="welcome-body">
        <p>There are times in life when you need the help of legal professionals who care.</p>
        <p>Here at Heritage Counsel we have a compassionate approach towards our clients who are often dealing with some of the most difficult situations life can serve up:</p>
        <ul>
          <li>• Death of a loved one</li>
          <li>• Aging family members</li>
          <li>• Buying or selling a home</li>
          <li>• Starting a new business</li>
          <li>• Negotiating a mortgage</li>
        </ul>
        <p>Even dealing with the everyday legal tasks associated with your business, aging parents or planning for the future can be stressful and our team are here to help with sound legal advice to help you find your way through.</p>
        <p>As a small team of dedicated professionals we aim to provide a friendly, family atmosphere with a reputation for timely, personalised service.</p>
      </div>
    </article>
    <div class="site-pill">www.heritagecounsel.com.au</div>
  </div>
  <div class="panel pocket-panel">
    <div class="pocket"></div>
  </div>
</section>
<div class="stage-label stage-label--inner">Inner</div>

</body>
</html>
```